Need Business Cards for my Business

email address: rkpmarlowhollowworks@vendrimail.com
web address: rkpmarlowhollowworks.net
Slogan: We offer various QVN licenses
Rowland K. Pemberly
Please stick with colors of Company Logo
would like the card to be more of the color example of the logo.
If you need PDF copy of logo email me at the above account.
Creative control rests with you.

Industry/Entity Type

Business

Contact Information for Business Card

I am a minimalist, but would like something to pop and stand out amongst other cards, make it memorable.

Font styles to use
Serif
Decorative
Script

```html
<!DOCTYPE html>
<html lang="en">
<head>
<meta charset="utf-8">
<title>RKP Marlow Hollow Works — Business Card</title>
<link href="https://fonts.googleapis.com/css2?family=Cinzel:wght@400;600&family=Questrial&family=Didact+Gothic&family=Montserrat:wght@600&display=swap" rel="stylesheet">
<style>
  :root {
    --canvas: #8f8f8f;
    --canvas-light: #a9a9a9;
    --card-white: #f2f2f2;
    --card-white-shade: #dcdcdc;
    --card-black: #050505;
    --sheen: #2c2c2c;
    --ink-dark: #111111;
    --ink-light: #ffffff;
    --ink-muted: #d6d6d6;
    --rule: #bdbdbd;
  }
  * { box-sizing: border-box; margin: 0; padding: 0; }
  html, body {
    width: 1200px;
    height: 1120px;
    overflow: hidden;
  }
  body {
    background: radial-gradient(ellipse at 50% 20%, var(--canvas-light), var(--canvas) 75%);
    display: flex;
    flex-direction: column;
    align-items: center;
    justify-content: center;
    gap: 46px;
  }
  .card {
    width: 860px;
    height: 491px;
    position: relative;
    box-shadow: 0 14px 30px rgba(0,0,0,0.35);
  }

  /* Front */
  .card--front {
    background: linear-gradient(160deg, var(--card-white) 40%, var(--card-white-shade));
    display: flex;
    align-items: center;
    justify-content: center;
  }
  .brand-name {
    font-family: "Questrial", sans-serif;
    font-size: 46px;
    letter-spacing: 3px;
    color: var(--ink-dark);
    text-transform: uppercase;
    text-align: center;
    line-height: 1.2;
  }

  /* Back */
  .card--back {
    background:
      linear-gradient(118deg, var(--card-black) 0 52%, var(--sheen) 62%, #161616 82%, #0b0b0b 100%);
    color: var(--ink-light);
    overflow: hidden;
  }
  .back-mark {
    position: absolute;
    left: 0;
    top: 0;
    width: 380px;
    height: 100%;
    display: flex;
    align-items: center;
    justify-content: center;
  }
  .back-mark .brand-name {
    color: var(--ink-light);
    font-size: 30px;
    letter-spacing: 2px;
  }
  .divider {
    position: absolute;
    left: 380px;
    top: 36px;
    width: 1px;
    height: 420px;
    background: var(--rule);
  }
  .contact {
    position: absolute;
    left: 414px;
    top: 36px;
    right: 30px;
  }
  .person-name {
    font-family: "Cinzel", serif;
    font-weight: 600;
    font-size: 27px;
    line-height: 1.08;
    letter-spacing: 1px;
    padding-bottom: 8px;
    border-bottom: 1px solid #555;
    width: 300px;
  }
  .person-title {
    font-family: "Didact Gothic", sans-serif;
    font-size: 17px;
    letter-spacing: 1px;
    margin-top: 8px;
    padding-left: 8px;
  }
  .phones {
    margin-top: 40px;
    padding-left: 32px;
    font-family: "Montserrat", sans-serif;
    font-weight: 600;
    font-size: 21px;
    line-height: 1.6;
    letter-spacing: 0.5px;
  }
  .details {
    margin-top: 10px;
    padding-left: 32px;
    font-family: "Didact Gothic", sans-serif;
    font-size: 16px;
    color: var(--ink-muted);
    line-height: 1.3;
  }
  .details p { margin-bottom: 14px; }
</style>
</head>
<body>
  <section class="card card--front" aria-label="Card front">
    <div class="brand-name">RKP Marlow<br>Hollow Works</div>
  </section>

  <section class="card card--back" aria-label="Card back">
    <div class="back-mark">
      <div class="brand-name">RKP Marlow<br>Hollow Works</div>
    </div>
    <div class="divider"></div>
    <div class="contact">
      <h1 class="person-name">Rowland<br>K. Pemberly</h1>
      <div class="person-title">President</div>
      <div class="phones">
        <div>400.000.0000</div>
        <div>600.000.0000</div>
      </div>
      <div class="details">
        <p>rkpmarlowhollowworks@vendrimail.com</p>
        <p>2270 Quillmere Ave, Ste 40<br>Harlow Bay, CA. 90217</p>
        <p>www.rkpmarlowhollowworks.net</p>
      </div>
    </div>
  </section>
</body>
</html>
```